Design an awesome Website mock-up for FurHaven

Good day Freelancers,

This is a pretty simple website but it must look great.
The details are in the document provided, if you have any questions please ask :)

Required: Website mock-up

Design must be professional, sleek, and modern.

Try to use colors that express safety, compassion, and positive vibes.

I will make another contest for the Logo Design.

```html
<!DOCTYPE html>
<html lang="en">
<head>
<meta charset="utf-8">
<title>FurHaven – Giving Pets a Chance</title>
<link rel="stylesheet" href="https://fonts.googleapis.com/css2?family=Ubuntu:wght@400;500;700&family=Roboto+Condensed:wght@300;400&family=Arimo:ital,wght@0,400;0,700;1,700&display=swap">
<style>
:root{
  --green:#3d9b16;
  --green-light:#6fcf2a;
  --green-dark:#2a7a0c;
  --orange:#f7931e;
  --orange-light:#fdb94a;
  --orange-dark:#e0700a;
  --page:#e8e8e8;
  --card:#ffffff;
  --text:#555;
  --text-light:#8a8a8a;
  --heading:#444;
  --footer:#1e1e1e;
}
*{box-sizing:border-box;margin:0;padding:0}
html,body{width:754px;height:1200px;overflow:hidden}
body{position:relative;background:radial-gradient(ellipse 420px 300px at 377px 220px,#fafafa,var(--page));font-family:"Arimo",sans-serif;color:var(--text)}
.abs{position:absolute}

/* header */
.brand{left:102px;top:15px;display:flex;align-items:center;gap:6px}
.brand-dot{width:22px;height:22px;border-radius:50%;background:var(--green)}
.brand-name{font-family:"Ubuntu",sans-serif;font-weight:700;font-size:25px;color:var(--orange)}
.account{right:102px;top:5px;display:flex;gap:4px}
.account a{display:block;font-family:"Ubuntu",sans-serif;font-size:10px;color:#fff;padding:2px 4px;border-radius:2px;text-decoration:none}
.btn-signin{background:linear-gradient(var(--green-light),var(--green))}
.btn-signup{background:linear-gradient(var(--orange-light),var(--orange))}
.hotline{right:101px;top:30px;text-align:right}
.hotline small{display:block;font-size:7px;color:#555;letter-spacing:.2px}
.hotline strong{display:flex;align-items:center;gap:4px;justify-content:flex-end;font-family:"Ubuntu",sans-serif;font-size:11.5px;color:var(--green);margin-top:3px}

/* nav */
.nav{left:102px;top:57px;width:552px;height:27px;border-radius:3px;background:linear-gradient(#5cc21f,#2f8f0c);box-shadow:0 2px 3px rgba(0,0,0,.25);display:flex;align-items:center}
.nav a{font-family:"Ubuntu",sans-serif;font-size:10px;color:#fff;text-decoration:none;height:100%;display:flex;align-items:center;padding:0 15px;border-right:1px solid rgba(255,255,255,.18)}
.nav a.active{background:linear-gradient(var(--orange-light),var(--orange));width:61px;justify-content:center;border-radius:3px 0 0 3px;padding:0}
.nav a:nth-child(4){border-right:0}
.search{margin-left:auto;margin-right:16px;width:90px;height:15px;border-radius:8px;background:#fff;font-size:6px;color:#bbb;padding:4px 5px}

/* hero */
.hero{left:102px;top:96px;width:552px;height:250px;border-radius:3px;overflow:hidden;box-shadow:0 1px 4px rgba(0,0,0,.2)}
.hero-photo{position:absolute;inset:0;background:linear-gradient(180deg,#5f8c2c 0%,#6a9c34 40%,#4b7d1e 100%)}
.hero-panel{position:absolute;inset:0;background:linear-gradient(160deg,var(--orange) 0%,var(--orange-light) 100%);clip-path:polygon(0 0,187px 0,271px 100%,0 100%);padding:30px 0 0 6px}
.hero h1{font-family:"Ubuntu",sans-serif;font-weight:700;font-size:15.5px;color:#fff}
.hero h1 span{color:#c94f00}
.hero p{font-size:7.4px;line-height:15px;color:#fff;margin:6px 0 0 9px;width:182px}
.hero p b{font-family:"Ubuntu",sans-serif;font-size:10px;color:#a44200;font-weight:500}
.hero ul{list-style:none;margin:2px 0 0 9px;font-size:7.6px;color:#fff;line-height:14px}
.hero li{padding-left:15px;position:relative;width:200px}
.hero li::before{content:"";position:absolute;left:1px;top:5px;width:5px;height:5px;background:#c25a00;transform:rotate(45deg)}
.btn-more{position:absolute;left:140px;top:219px;width:87px;height:21px;border-radius:3px;background:linear-gradient(#5cc21f,#2f8f0c);color:#fff;font-family:"Ubuntu",sans-serif;font-weight:700;font-size:11px;display:flex;align-items:center;justify-content:center;gap:5px;box-shadow:0 1px 2px rgba(0,0,0,.3)}
.btn-more i{width:10px;height:10px;border-radius:50%;border:1.5px solid #fff}
.dots{left:358px;top:351px;display:flex;gap:2px}
.dots span{width:10px;height:10px;border-radius:50%;background:#e3e3e3;border:1px solid #bbb}
.dots span.on{background:var(--green);border-color:var(--green)}

.section-title{left:0;width:754px;top:373px;text-align:center;font-family:"Ubuntu",sans-serif;font-weight:500;font-size:18px;color:var(--green)}

/* cases */
.case{width:179px;height:148px;background:var(--card);border-radius:3px;box-shadow:0 1px 4px rgba(0,0,0,.15)}
.case h3{font-family:"Roboto Condensed",sans-serif;font-weight:300;font-size:13px;color:#333;text-align:center;margin-top:12px}
.case-photo{position:absolute;left:6px;top:37px;width:72px;height:66px}
.case-text{position:absolute;left:86px;top:37px;width:88px;font-size:7.6px;line-height:10.5px;color:#555}
.case-text b{color:var(--green)}
.case-text .need{display:block;margin-top:4px;padding-left:0}
.raised{position:absolute;left:15px;top:110px;font-size:7px;color:#333}
.bar{position:absolute;left:13px;top:121px;width:150px;height:15px;border:1px solid #5cbf2a;border-radius:2px;background:#fff;overflow:hidden}
.bar i{display:block;height:100%;background:linear-gradient(#8be04a,#3ea10e)}
.read{position:absolute;left:61px;top:141px;width:57px;height:19px;border-radius:3px;background:linear-gradient(var(--orange-light),var(--orange-dark));color:#fff;font-size:8px;display:flex;align-items:center;justify-content:center;box-shadow:0 1px 2px rgba(0,0,0,.25)}
.pager{left:0;width:754px;top:756px;display:flex;justify-content:center;gap:6px;font-family:"Ubuntu",sans-serif;font-size:9.5px;color:var(--green);align-items:center}
.pager .cur{background:var(--green);color:#fff;border-radius:2px;padding:0 3px}

.rule{left:102px;width:552px;height:1px;background:#d7d7d7;border-bottom:1px solid #fff}

/* about */
.about{left:102px;top:788px;width:166px}
.h2{font-family:"Ubuntu",sans-serif;font-size:16px;color:var(--heading)}
.h2 span{color:var(--green);font-weight:500}
.about .lead{font-size:7.2px;line-height:10.5px;font-weight:700;color:var(--green);margin-top:12px}
.about .body{font-size:6.8px;line-height:10.4px;color:var(--text-light);margin-top:7px}
.about .more{display:block;text-align:right;font-size:6.5px;color:var(--green);text-decoration:underline;margin-top:9px}
.team{left:287px;top:788px}
.members{display:flex;gap:7px;margin-top:13px}
.member{width:86px}
.member .photo{height:90px;border:1px solid #ddd;background:linear-gradient(180deg,#f3f3f3,#dedede)}
.member b{display:block;font-style:italic;font-size:8.5px;color:#333;margin-top:7px}
.member span{display:block;font-size:8px;color:#555;margin-top:2px}

/* testimonials */
.testimonials{left:102px;top:970px}
.quotes{display:flex;gap:7px;margin-top:10px}
.quote{width:132px}
.quote .box{position:relative;height:110px;border:1px solid #d8d8d8;border-radius:3px;background:#efefef;padding:15px 10px 0 12px;font-size:7px;line-height:10.5px;color:#aaa}
.quote .box::after{content:"";position:absolute;right:14px;bottom:-6px;width:10px;height:10px;background:#efefef;border-right:1px solid #d8d8d8;border-bottom:1px solid #d8d8d8;transform:rotate(45deg)}
.quote .box b{color:#555;font-size:9px;margin-right:3px}
.quote.first .box{color:var(--green);font-weight:700}
.quote .who{text-align:right;padding-right:14px;margin-top:10px;font-size:8px;line-height:12px;color:#444}
.quote .who i{font-weight:700}

/* footer */
.footer{left:0;top:1160px;width:754px;height:40px;background:var(--footer)}
.footer .brand{left:102px;top:9px}
.footer .brand-name{color:#fff;font-size:17px}
.footer .brand-dot{width:16px;height:16px;background:#fff}
.footer nav{position:absolute;left:288px;top:7px;font-size:6.8px;color:#aaa}
.footer nav span{padding:0 4px;border-left:1px solid #777}
.footer nav span:first-child{border:0;padding-left:0}
.footer .copy{position:absolute;left:300px;top:24px;font-size:6.5px;color:#888}
.social{position:absolute;left:601px;top:11px;display:flex;gap:1px}
.social i{width:12px;height:12px;background:#ddd;border-radius:1px}
</style>
</head>
<body>

<header>
  <div class="abs brand"><span class="brand-dot"></span><span class="brand-name">FurHaven</span></div>
  <div class="abs account"><a class="btn-signin" href="#">Sign in</a><a class="btn-signup" href="#">Sign up</a></div>
  <div class="abs hotline">
    <small>HAVE A PROBLEM WITH YOUR PET?</small>
    <strong><svg width="9" height="11" viewBox="0 0 9 11"><rect width="9" height="11" rx="1.5" fill="#333"/><path d="M2.5 2.5c0 3 1.5 5 4 6l.8-1.2-1.4-.9-.6.6c-1-.6-1.5-1.5-1.7-2.6l.8-.3-.3-1.7z" fill="#fff"/></svg>1-800-555-0186</strong>
  </div>
  <nav class="abs nav">
    <a class="active" href="#">Home</a><a href="#">How we work</a><a href="#">Help &amp; Support</a><a href="#">Contacts Us</a>
    <div class="search">SEARCH</div>
  </nav>
</header>

<section class="abs hero">
  <div class="hero-photo" role="img" aria-label="Golden retriever playing with a ball on a green lawn"></div>
  <div class="hero-panel">
    <h1>Welcome to <span>FurHaven</span></h1>
    <p><b>FurHaven</b> is a non-profit organization that collects funds by using crowd-funding techniques via the web, transfers it to the dog shelter or veterinarian (if it is a surgery), and checks that the money goes where it is supposed to go.</p>
    <ul>
      <li>Shelters</li><li>Food</li><li>Medicines</li><li>Vaccinations, surgeries, etc</li>
      <li>Travel costs that are incurred when adopted by someone overseas</li>
    </ul>
  </div>
  <div class="btn-more">Read More <i></i></div>
</section>
<div class="abs dots"><span class="on"></span><span></span><span></span></div>

<h2 class="abs section-title">Giving Pets a Chance when money is tight</h2>

<article class="abs case" style="left:102px;top:407px">
  <h3>Surgery to walk and play again!</h3>
  <div class="case-photo" role="img" aria-label="Small black and white dog" style="background:linear-gradient(#c9c9c9,#6a6a6a)"></div>
  <p class="case-text"><b>Takota</b> is one of Lorem ipsum dolor sit amet, consectetuer adipiscing elit.<span class="need">Needed by: In the next few months</span></p>
  <span class="raised">Raised: $1,106.00</span><div class="bar"><i style="width:27%"></i></div><a class="read">read more</a>
</article>
<article class="abs case" style="left:288px;top:407px">
  <h3>Surgery to walk and play again!</h3>
  <div class="case-photo" role="img" aria-label="Brown and white bulldog face" style="background:linear-gradient(#c89a72,#8a5a3a)"></div>
  <p class="case-text"><b>Takota</b> is one of Lorem ipsum dolor sit amet, consectetuer adipiscing elit.<span class="need">Needed by: In the next few months</span></p>
  <span class="raised">Raised: $1,106.00</span><div class="bar"><i style="width:77%"></i></div><a class="read">read more</a>
</article>
<article class="abs case" style="left:475px;top:407px">
  <h3>Surgery to walk and play again!</h3>
  <div class="case-photo" role="img" aria-label="Dark shepherd puppy sitting indoors" style="background:linear-gradient(#8a8f98,#3a3d44)"></div>
  <p class="case-text"><b>Takota</b> is one of Lorem ipsum dolor sit amet, consectetuer adipiscing elit.<span class="need">Needed by: In the next few months</span></p>
  <span class="raised">Raised: $1,106.00</span><div class="bar"><i style="width:52%"></i></div><a class="read">read more</a>
</article>

<article class="abs case" style="left:102px;top:586px">
  <h3>Surgery to walk and play again!</h3>
  <div class="case-photo" role="img" aria-label="Dog resting in a living room" style="background:linear-gradient(#b07a50,#5a3020)"></div>
  <p class="case-text"><b>Takota</b> is one of Lorem ipsum dolor sit amet, consectetuer adipiscing elit.<span class="need">Needed by: In the next few months</span></p>
  <span class="raised">Raised: $1,106.00</span><div class="bar"><i style="width:53%"></i></div><a class="read">read more</a>
</article>
<article class="abs case" style="left:288px;top:586px">
  <h3>Surgery to walk and play again!</h3>
  <div class="case-photo" role="img" aria-label="Golden retriever sitting" style="background:linear-gradient(#e0c49a,#b08650)"></div>
  <p class="case-text"><b>Takota</b> is one of Lorem ipsum dolor sit amet, consectetuer adipiscing elit.<span class="need">Needed by: In the next few months</span></p>
  <span class="raised">Raised: $1,106.00</span><div class="bar"><i style="width:75%"></i></div><a class="read">read more</a>
</article>
<article class="abs case" style="left:475px;top:586px">
  <h3>Surgery to walk and play again!</h3>
  <div class="case-photo" role="img" aria-label="Tan dog sitting on a floor" style="background:linear-gradient(#a87852,#5e3a22)"></div>
  <p class="case-text"><b>Takota</b> is one of Lorem ipsum dolor sit amet, consectetuer adipiscing elit.<span class="need">Needed by: In the next few months</span></p>
  <span class="raised">Raised: $1,106.00</span><div class="bar"><i style="width:95%"></i></div><a class="read">read more</a>
</article>

<div class="abs pager"><span>PREV</span><span class="cur">1</span><span>2</span><span>3</span><span>4....NEX</span></div>

<div class="abs rule" style="top:777px"></div>

<section class="abs about">
  <h2 class="h2">About our <span>FurHaven</span>:</h2>
  <p class="lead">Vivamus hendrerit mauris ut dui gravida ut viverra lectus tincidunt. Cras mattis tempor eros nec tristique.</p>
  <p class="body">Sed sed felis arcu, vel vehicula augue. Maecenas faucibus sagittis cursus. Fusce tincidunt, tellus eget tristique cursus, orci mi iaculis sem, sit amet dictum velit velit eu magna. Nunc viverra nisi sed orci tincidunt at hendrerit orci luctus. Andisse tincidunt, ipsum at semper facilisis.</p>
  <a class="more">READ MORE</a>
</section>

<section class="abs team">
  <h2 class="h2">Meet our team:</h2>
  <div class="members">
    <div class="member"><div class="photo" role="img" aria-label="Portrait of the team surgeon"></div><b>Owen Hartley</b><span>(surgeon)</span></div>
    <div class="member"><div class="photo" role="img" aria-label="Portrait of the team nurse"></div><b>Maya Linden</b><span>(nurse)</span></div>
    <div class="member"><div class="photo" role="img" aria-label="Portrait of the team diagnostician"></div><b>Nora Vance</b><span>(diagnostician)</span></div>
    <div class="member"><div class="photo" role="img" aria-label="Portrait of the team immunologist"></div><b>Peter Aldous</b><span>(immunologist)</span></div>
  </div>
</section>

<div class="abs rule" style="top:960px"></div>

<section class="abs testimonials">
  <h2 class="h2" style="font-size:19px;font-weight:400">Testimonials:</h2>
  <div class="quotes">
    <div class="quote first"><div class="box"><b>«</b>Sed sed felis arcu, vel vehicula augue. Maecenas faucibus sagittis cursus. Fusce tincidunt, tellus eget tristique cursus orci mi iaculis sem sit. amet dictum velit velit eu magna. Nuviverra <b>»</b></div><p class="who"><i>Daniel Shore</i><br>(manager)</p></div>
    <div class="quote"><div class="box"><b>«</b>Sed sed felis arcu, vel vehicula augue. Maecenas faucibus sagittis cursus. Fusce tincidunt, tellus eget tristique cursus orci mi iaculis sem sit amet dictum velit velit eu. <b>»</b></div><p class="who"><i>Emily Rowan</i><br>(housewife)</p></div>
    <div class="quote"><div class="box"><b>«</b>Maecenas faucibus sagittis cursus. Fusce tincidunt, tellus eget tristique cursus orci mi iaculis sem sit. amet dictum velit velit eu magna. Nunc viverra nisi sed orci tin. <b>»</b></div><p class="who"><i>Victor Lane</i><br>(lawyer)</p></div>
    <div class="quote"><div class="box"><b>«</b>Fusce tincidunt, tellus eget tristique cursus orci mi iaculis sem sit. amet dictum velit velit eu magna. Nunc viverra nisi sed orci tincidunt at hendrerit orci luctus. Andisse tincidunt, ipsu. <b>»</b></div><p class="who"><i>Marc Ellery</i><br>(manager)</p></div>
  </div>
</section>

<footer class="abs footer">
  <div class="abs brand"><span class="brand-dot"></span><span class="brand-name">FurHaven</span></div>
  <nav><span>Home</span><span>How it work</span><span>Help &amp; Support</span><span>Contact Us</span></nav>
  <p class="copy">© 2013 by furhaven.org &nbsp; All Right Reserved</p>
  <div class="social"><i></i><i></i><i></i><i></i></div>
</footer>

</body>
</html>
```